VBN Line Card

We are looking for a line card to leave with potential customers.
Logo on top

VBN is a Colorado-based business specializing in demolition, materials management, hazardous materials management, and trucking & hauling. What differentiates VBN is our breadth of experience in upcycling much of reusable debris from the demolition process for reuse on existing projects or recycling the material for later use on other projects.

We offer an end-to-end client experience that includes seamless communication, budgeting, staffing, on-site organization, and solid, quality work every time.

Trucking and Hauling Equipment:
30 yd End Dump
Steel Side Scrap Trailer
90 yr End Dump
Flatbeds
70 Ton Lowboy Trailer 2-3-2 combo

Gordon Ellery
President
720-463-9170
gellery@vbnmetalworks.com

I'd like it to be easy to read, but look modern

Target Market(s)

General Contractors

Industry/Entity Type

Construction

Colors
EB3D1F
EC4F4E
F09395
F8D3D4
FCEDEE

Requirements
Must have
• Our colors and red and gun metal gray

```html
<!DOCTYPE html>
<html lang="en">
<head>
<meta charset="utf-8">
<title>VBN Line Card</title>
<link href="https://fonts.googleapis.com/css2?family=Kanit:ital,wght@0,500;0,600;0,700;1,500;1,600;1,700&display=swap" rel="stylesheet">
<style>
  :root {
    --brand-red: #8c1b20;
    --brand-red-bright: #eb3d1f;
    --gunmetal: #222226;
    --gunmetal-light: #2c2c31;
    --paper: #ffffff;
    --mist: #ecedf0;
    --rule: #c9c9cc;
    --stage: #c4c4c4;
    --ink: #1c1c1f;
  }
  * { margin: 0; padding: 0; box-sizing: border-box; }
  html, body { width: 795px; height: 1200px; overflow: hidden; }
  body {
    background: var(--stage);
    font-family: "Kanit", sans-serif;
    color: var(--ink);
    position: relative;
  }
  .line-card {
    position: absolute;
    left: 25px; top: 334px;
    width: 745px; height: 532px;
    background: var(--paper);
    overflow: hidden;
  }
  .card-shapes { position: absolute; inset: 0; width: 745px; height: 532px; }
  .wordmark {
    position: absolute;
    left: 32px; top: 28px;
    font-weight: 700;
    font-size: 54px;
    line-height: 1;
    letter-spacing: 6px;
    color: var(--brand-red);
  }
  .offer-heading {
    position: absolute;
    left: 34px; top: 118px;
    height: 34px;
    font-weight: 700; font-style: italic;
    font-size: 24px; line-height: 34px;
    color: var(--paper);
  }
  .offer-list { position: absolute; left: 32px; top: 156px; list-style: none; }
  .offer-list li {
    position: relative;
    padding-left: 18px;
    font-weight: 600; font-style: italic;
    font-size: 17px; line-height: 30px;
    height: 31px;
    border-bottom: 1px solid var(--rule);
    width: max-content;
    padding-right: 20px;
  }
  .offer-list li::before {
    content: "";
    position: absolute; left: 1px; top: 11px;
    width: 7px; height: 7px; border-radius: 50%;
    background: var(--brand-red);
  }
  .offer-list li.no-rule { border-bottom: none; }
  .offer-list li.continued::before { display: none; }
  .photo-area { position: absolute; inset: 0; }
  .contact-name {
    position: absolute;
    left: 32px; top: 407px;
    font-weight: 700; font-style: italic;
    font-size: 22px; line-height: 35px;
    color: var(--paper);
    letter-spacing: 0.5px;
  }
  .contact-details {
    position: absolute; left: 32px; top: 450px;
    color: var(--paper); font-style: italic;
  }
  .contact-role { font-weight: 600; font-size: 14px; line-height: 22px; }
  .contact-line {
    display: flex; align-items: center; gap: 6px;
    font-size: 15px; line-height: 25px; font-weight: 600;
  }
  .contact-line.phone { font-weight: 700; font-size: 16px; }
  .contact-line svg { width: 11px; height: 11px; flex: none; }
  .equipment { position: absolute; left: 0; top: 0; color: var(--paper); font-style: italic; }
  .equipment p { position: absolute; white-space: nowrap; font-size: 14px; line-height: 18px; font-weight: 500; }
  .equipment .equipment-title { font-weight: 700; }
  .watermark-name {
    position: absolute; left: 610px; top: 436px;
    font-weight: 700; font-size: 40px; line-height: 1;
    letter-spacing: 5px; color: var(--gunmetal-light);
  }
</style>
</head>
<body>
  <main class="line-card">
    <svg class="card-shapes" viewBox="0 0 745 532" aria-hidden="true">
      <defs>
        <linearGradient id="photo-tones" x1="0" y1="0" x2="0" y2="1">
          <stop offset="0" stop-color="#2f5e6b"/>
          <stop offset="0.3" stop-color="#e98b95"/>
          <stop offset="0.6" stop-color="#b8323a"/>
          <stop offset="1" stop-color="#f0743a"/>
        </linearGradient>
      </defs>
      <polygon class="mist-band" points="335,0 537,0 300,132 130,132" fill="var(--mist)"/>
      <polygon class="offer-band" points="0,118 231,118 201,152 0,152" fill="var(--brand-red)"/>
      <polygon class="red-panel" points="0,391 391,391 298,532 0,532" fill="var(--brand-red)"/>
      <polygon class="gunmetal-panel" points="397,391 745,391 745,532 305,532" fill="var(--gunmetal)"/>
      <rect class="gunmetal-edge" x="300" y="524" width="445" height="8" fill="var(--brand-red)"/>
      <polygon class="name-band" points="0,407 257,407 233,442 0,442" fill="var(--gunmetal)"/>
      <polygon class="name-band-edge" points="257,407 261,407 237,442 233,442" fill="var(--brand-red-bright)"/>
    </svg>

    <svg class="photo-area" viewBox="0 0 745 532" role="img" aria-label="Photo of a red semi truck with a box trailer driving on a sunlit road">
      <polygon points="537,0 745,0 745,382 312,382 227,309" fill="url(#photo-tones)"/>
    </svg>

    <div class="wordmark">VBN</div>

    <h2 class="offer-heading">WE OFFER</h2>
    <ul class="offer-list">
      <li>Seamless communication</li>
      <li>Budgeting</li>
      <li>Staffing</li>
      <li>On-Site Organization</li>
      <li>And solid</li>
      <li class="no-rule">Quality Work</li>
      <li class="no-rule continued">Every Time</li>
    </ul>

    <h1 class="contact-name">GORDON ELLERY</h1>
    <div class="contact-details">
      <p class="contact-role">President</p>
      <p class="contact-line phone">
        <svg viewBox="0 0 12 12" aria-hidden="true"><path d="M3 1h2l1 3-1.5 1a6 6 0 0 0 2.5 2.5L8 6l3 1v2a1.5 1.5 0 0 1-1.5 1.5A8.5 8.5 0 0 1 1.5 2.5 1.5 1.5 0 0 1 3 1z" fill="none" stroke="currentColor" stroke-width="1"/></svg>
        720-463-9170
      </p>
      <p class="contact-line">
        <svg viewBox="0 0 12 12" aria-hidden="true"><rect x="1" y="2.5" width="10" height="7" fill="none" stroke="currentColor" stroke-width="1"/><path d="M1 2.5l5 4 5-4" fill="none" stroke="currentColor" stroke-width="1"/></svg>
        gellery@vbnmetalworks.com
      </p>
    </div>

    <div class="watermark-name" aria-hidden="true">VBN</div>

    <section class="equipment">
      <p class="equipment-title" style="left:416px;top:402px;">Trucking and Hauling Equipment:</p>
      <p style="left:402px;top:420px;">30 yd End Dump</p>
      <p style="left:391px;top:438px;">Steel Side Scrap Trailer</p>
      <p style="left:379px;top:456px;">90 yr End Dump</p>
      <p style="left:366px;top:474px;">Flatbeds</p>
      <p style="left:355px;top:492px;">70 Ton Lowboy Trailer 2-3-2 combo</p>
    </section>
  </main>
</body>
</html>
```